Placing my newer logo on my existing business card

I have a business card that I had you guys do years ago, then I changed my logo, I love both my business card and my logo. The challenge is both my logo and my business card are very similar in color. So I'm not sure how to make my logo stand out.

Sick

```html
<!DOCTYPE html>
<html lang="en">
<head>
<meta charset="utf-8">
<title>Bramblewell Weight &amp; Hormone Clinic – Card Set</title>
<link rel="stylesheet" href="https://fonts.googleapis.com/css2?family=Cinzel:wght@500&family=Tinos:wght@400;700&family=Italianno&display=swap">
<style>
  :root{
    --stage:#929397;
    --ink:#111;
    --rust:#a84e2a;
    --copper:#a95c34;
    --blush:#d49a85;
    --wine:#55111a;
    --sky-top:#ffffff;
    --sky-mid:#cfe9f5;
    --sky-low:#86cbe9;
    --bullet:#6a6fb0;
    --mark:#6b9fa8;
  }
  *{box-sizing:border-box;margin:0;padding:0}
  html,body{width:1200px;height:800px;overflow:hidden;background:var(--stage)}
  body{position:relative;font-family:"Tinos","Times New Roman",serif;color:var(--ink)}
  .card{position:absolute;width:563px;height:329px;overflow:hidden;
        background:linear-gradient(180deg,var(--sky-top) 0%,var(--sky-mid) 50%,var(--sky-low) 100%)}
  .card--front{left:22px;top:55px}
  .card--director{left:615px;top:55px;background:linear-gradient(180deg,#fff 0%,#cfe8f6 45%,#74bfe8 100%)}
  .card--appointment{left:24px;top:415px;background:linear-gradient(180deg,var(--copper) 0%,#c07a58 30%,var(--blush) 50%,#8b3a2c 78%,var(--wine) 100%)}
  .card--conditions{left:615px;top:415px}
  .abs{position:absolute}
  .center{text-align:center}

  /* Wordmark: plain text, one colour, one weight, with a plain circle */
  .wordmark{position:absolute;display:flex;flex-direction:column;align-items:center;gap:8px}
  .wordmark .dot{width:22px;height:22px;border-radius:50%;background:var(--mark)}
  .wordmark .name{font-family:"Tinos",serif;font-weight:400;color:var(--rust);line-height:1.15;text-align:center}

  .label{color:var(--rust)}
  .front-mark{left:0;width:412px;top:62px}
  .front-mark .name{font-size:22px}
  .front-contact{left:0;width:412px;top:180px;font-size:16px;line-height:23px}
  .divider{position:absolute;left:60px;width:294px;top:236px;height:1px;background:#333}
  .divider::after{content:"";position:absolute;left:142px;top:-3px;width:7px;height:7px;border-radius:50%;background:#111}
  .front-address{left:0;width:412px;top:247px;font-size:16px;line-height:22px}
  .ribbon{position:absolute;right:0;top:0;width:180px;height:329px}

  .director-mark{left:0;width:368px;top:40px}
  .director-mark .dot{width:20px;height:20px}
  .director-mark .name{font-size:17px}
  .person{left:0;width:368px;top:146px;font-size:27px;font-weight:700}
  .role{left:0;width:368px;top:178px;font-size:14px;color:var(--rust)}
  .director-info{left:0;width:368px;top:203px;font-size:15px;line-height:19.5px}
  .director-info p+p{margin-top:12px}
  .portrait{position:absolute;right:0;top:0;width:215px;height:329px;
            background:linear-gradient(90deg,rgba(255,255,255,0) 0%,#d9cdbd 25%,#bfa68c 60%,#a99079 100%)}

  .appt-panel{position:absolute;left:29px;top:53px;width:505px;height:247px;
              background:linear-gradient(180deg,#fff 0%,#d2ebf6 45%,#8dcbea 100%)}
  .appt-mark{position:absolute;left:0;width:563px;top:20px;display:flex;justify-content:center;align-items:center;gap:7px}
  .appt-mark .dot{width:10px;height:10px;border-radius:50%;background:#fff}
  .appt-mark .name{font-size:14px;color:#fff}
  .appt-title{left:0;width:563px;top:98px;font-family:"Cinzel",serif;font-size:16px;letter-spacing:.06em;text-align:center;color:#1a1a1a}
  .field{position:absolute;top:180px;font-size:15px;display:flex;align-items:flex-end}
  .field .line{display:inline-block;height:1px;background:#111;margin-left:6px;margin-bottom:4px}
  .slogan{left:0;width:563px;top:250px;font-family:"Italianno",cursive;font-size:40px;text-align:center;line-height:1}
  .swirl-fade{position:absolute;right:40px;top:0;width:120px;height:329px;
              background:linear-gradient(90deg,rgba(255,255,255,0) 0%,rgba(196,170,160,.35) 50%,rgba(255,255,255,0) 100%)}

  .cond-title{left:0;width:563px;top:21px;text-align:center;font-weight:700;font-size:16.5px;letter-spacing:.02em}
  .cond-list{position:absolute;top:44px;list-style:none;font-size:14px;line-height:17.7px}
  .cond-list li{position:relative;padding-left:17px}
  .cond-list li::before{content:"";position:absolute;left:0;top:6px;width:7px;height:7px;border-radius:50%;background:var(--bullet)}
  .cond-list--left{left:44px}
  .cond-list--right{left:334px}
  .cond-rule{position:absolute;left:44px;width:475px;top:248px;height:1px;background:#111}
  .foot-mark{left:86px;width:105px;top:256px;gap:4px}
  .foot-mark .dot{width:12px;height:12px;background:#333}
  .foot-mark .name{font-size:9px;color:#222}
  .call{left:205px;top:258px;font-size:22px;line-height:1}
  .call-web{left:205px;top:286px;font-size:14px}
</style>
</head>
<body>

  <section class="card card--front">
    <div class="wordmark front-mark"><span class="dot"></span><span class="name">Bramblewell Weight<br>&amp; Hormone Clinic</span></div>
    <div class="abs center front-contact">
      <p><span class="label">PH:</span> (555) 201-4470 &nbsp;|&nbsp; <span class="label">FX:</span> (555)201-4471</p>
      <p>bramblewellclinic.com</p>
    </div>
    <div class="divider"></div>
    <div class="abs center front-address"><p>1480 cedar ave ste#3</p><p>north harbor ut 84022</p></div>
    <svg class="ribbon" viewBox="0 0 180 329" role="img" aria-label="Flowing copper ribbon with swirl ornaments">
      <defs>
        <linearGradient id="ribbonFill" x1="0" y1="0" x2="0" y2="1">
          <stop offset="0" stop-color="#a95c34"/>
          <stop offset=".45" stop-color="#d49a85"/>
          <stop offset=".75" stop-color="#8b3a2c"/>
          <stop offset="1" stop-color="#55111a"/>
        </linearGradient>
      </defs>
      <path d="M18 0 C70 30 70 90 40 150 C10 210 20 280 60 329 L180 329 L180 0 Z" fill="url(#ribbonFill)"/>
    </svg>
  </section>

  <section class="card card--director">
    <div class="wordmark director-mark"><span class="dot"></span><span class="name">Bramblewell Weight<br>&amp; Hormone Clinic</span></div>
    <div class="abs center person">Marla Hendricks</div>
    <div class="abs center role">Director</div>
    <div class="abs center director-info">
      <p>1480 Cedar Ave ste#3<br>north Harbor Utah 84022</p>
      <p>1(555)201-4470<br>www.bramblewellclinic.com</p>
    </div>
    <div class="portrait" role="img" aria-label="Photo of the director in a white coat beside a brick wall"></div>
  </section>

  <section class="card card--appointment">
    <div class="appt-panel"></div>
    <div class="swirl-fade" role="img" aria-label="Faint copper swirl ornament"></div>
    <div class="appt-mark"><span class="dot"></span><span class="name">Bramblewell Weight &amp; Hormone Clinic</span></div>
    <div class="abs appt-title">APPOINTMENT ON....</div>
    <div class="field" style="left:46px">Time<span class="line" style="width:173px"></span></div>
    <div class="field" style="left:265px">Date<span class="line" style="width:213px"></span></div>
    <div class="abs slogan">Let’s Make it Happen</div>
  </section>

  <section class="card card--conditions">
    <div class="swirl-fade" style="right:30px" role="img" aria-label="Faint copper swirl ornament"></div>
    <div class="abs cond-title">Conditions we address for women and men</div>
    <ul class="cond-list cond-list--left">
      <li>PCOS</li><li>Hysterectomy</li><li>Type-II Diabetes</li><li>Insulin Resistance</li>
      <li>Hypothyroid</li><li>Underactive Thyroid</li><li>Fibromyalgia</li><li>Chronic Fatigue</li>
      <li>Chronic Headaches &amp; Migraines</li><li>Hypertension</li><li>Elevated Fasting Glucose</li>
    </ul>
    <ul class="cond-list cond-list--right">
      <li>Pre-Diabetes</li><li>Abdominal Obesity</li><li>High Triglycerides</li><li>High Blood Pressure</li>
      <li>High Cholesterol</li><li>Gestational Diabetes</li><li>Epstein Bar</li><li>Infertility</li>
      <li>Infertility Drugs</li><li>Anti-Depression Medications</li>
    </ul>
    <div class="cond-rule"></div>
    <div class="wordmark foot-mark"><span class="dot"></span><span class="name">Bramblewell Weight<br>&amp; Hormone Clinic</span></div>
    <div class="abs call">Call Today!: (555)201-4470</div>
    <div class="abs call-web">www.bramblewellclinic.com</div>
  </section>

</body>
</html>
```